A wordpress website for the coolest Resort App

We have developed a mobile app - Zapply and we want to develop a cool, neat and simple wordpress website for it.

I have attached the basics in a keynote/ ppt - but i need you to bring it more to life. plus there are additions:

FOr the number of pages, we will have:
1- Home: very similar to the one pager
2- How it works: Showing step by step on how the app works, and how it connects to the POS system of the restaurant etc with spanshots from the app
3- Benefit: Elaborating more on each of the benefits that is mentioned in the ONE PAGE document, with additional statistics, reference etc.. and embedded videos and animation
4- who we are page
5- In the press page: links to the articles where zapply was mentioned
6- Get in touch page
7- FAQ
Updates

Project Deadline Extended Reason: The first deadline was set for the 1 page website, now i am extending it for the full wesbite development.Still i need the one pager by the 17th, but for the rest we have more time Added Friday, September 15, 2017

Target Market(s)

Resorts, hotels, beach and pool restaurant operators

Industry/Entity Type

Hospitality

Coding

Coded - Design and coding required

Font styles to use
Other font styles liked:
• I have attached the fonts i want to use: ROboto is the main font

Colors

Designer to choose colors to be used in the design.

Requirements
Must have
• Logo, icons for each benefit, you can also use the mood picture i attached or any other picture you recommend - maybe just something related to the app
• I also attached the Main colour, the orange and the blue is the accent one
• I attached the fonts, roboto is the main one
• there should also be a contact us:
• Email : info@zapplyhub.example
• Mobile: +971 5 23 47 90 12
• Address: Harbor Quarter - Dubai - United Arab Emirates

```html
<!DOCTYPE html>
<html lang="en">
<head>
<meta charset="utf-8">
<title>Zapply – Resort App</title>
<link href="https://fonts.googleapis.com/css2?family=Roboto:wght@400;500;700;900&family=Open+Sans:wght@400;600;700&display=swap" rel="stylesheet">
<style>
:root{
  --orange:#f47a4f;
  --orange-dark:#e8643a;
  --blue:#2e9ad7;
  --blue-dark:#1f7fb9;
  --ink:#2b2b2b;
  --text:#555;
  --muted:#8a8a8a;
  --line:#d9d9d9;
  --dark:#2c2c2c;
  --darker:#1f1f1f;
  --white:#fff;
}
*{margin:0;padding:0;box-sizing:border-box}
html,body{width:1200px;height:4455px;overflow:hidden}
body{font-family:"Roboto",sans-serif;color:var(--ink);background:var(--white)}
section,header,footer{position:relative;width:1200px;overflow:hidden}
.abs{position:absolute}
.center-x{left:0;right:0;text-align:center}
.section-title{position:absolute;left:0;right:0;text-align:center;font-family:"Roboto",sans-serif;font-weight:700;font-size:28px;letter-spacing:.5px;text-transform:uppercase}
.lead{position:absolute;left:240px;width:720px;text-align:center;font-family:"Open Sans",sans-serif;font-size:12.5px;line-height:20px;color:var(--muted)}

/* header */
.site-header{height:105px;background:var(--white)}
.brand{position:absolute;display:flex;align-items:center;gap:14px;font-family:"Roboto",sans-serif;font-weight:700}
.brand-dot{width:40px;height:40px;border-radius:50%;background:var(--orange)}
.site-header .brand{left:100px;top:28px;font-size:44px;color:var(--ink)}
.topbar{position:absolute;right:100px;top:14px;font-size:13px;color:var(--text);display:flex;align-items:center;gap:10px}
.topbar svg{width:14px;height:14px}
.topbar .sep{color:var(--line);margin:0 6px}
.nav{position:absolute;right:100px;top:56px;display:flex;gap:28px;font-size:14px;font-weight:500;color:var(--ink)}
.nav a{text-decoration:none;color:inherit;padding-bottom:6px}
.nav a.active{color:var(--orange);border-bottom:2px solid var(--orange)}

/* hero */
.hero{height:623px}
.hero-photo{position:absolute;inset:0;background:linear-gradient(180deg,#7fb9e2 0%,#a9d4ec 30%,#4fb7c8 48%,#2f9fb0 60%,#e9dcc4 78%,#d9c6a6 100%)}
.hero-word{position:absolute;top:320px;left:0;right:0;text-align:center;color:var(--white);font-size:84px;font-weight:700;letter-spacing:1px}
.hero-wave{position:absolute;left:0;bottom:0;width:1200px;height:110px}
.hero-dots{position:absolute;top:560px;left:0;right:0;display:flex;justify-content:center;gap:8px}
.hero-dots span{width:12px;height:12px;border-radius:50%;border:2px solid var(--orange);background:var(--white)}
.hero-dots span.on{background:var(--orange)}

/* how it works */
.how{height:802px}
.phone{position:absolute;left:535px;top:222px;width:130px;height:274px;border-radius:22px;background:#f3f3f3;border:2px solid #cfcfcf}
.phone .screen{position:absolute;left:9px;top:36px;width:108px;height:196px;background:var(--orange);display:flex;align-items:center;justify-content:center;color:var(--white);font-weight:700;font-size:18px}
.phone .cam{position:absolute;left:50px;top:16px;width:26px;height:4px;border-radius:2px;background:#cfcfcf}
.phone .btn{position:absolute;left:51px;top:241px;width:24px;height:24px;border-radius:50%;border:2px solid #cfcfcf}
.step{position:absolute;width:180px;margin-left:-90px;text-align:center}
.step .badge{width:112px;height:112px;margin:0 auto}
.step-label{margin-top:10px;font-size:12.5px;font-weight:500;line-height:17px;text-transform:uppercase;color:var(--ink)}
.flow{position:absolute;left:0;top:0;width:1200px;height:802px}

/* benefits */
.benefits{height:772px;color:var(--white)}
.benefits-photo{position:absolute;inset:0;background:radial-gradient(ellipse at 50% 45%,#5a4a3c 0%,#2a2420 45%,#141414 100%)}
.benefits .section-title{top:56px;color:var(--white)}
.tabs{position:absolute;top:126px;left:445px;display:flex;gap:24px}
.tab{height:34px;padding:0 18px;font-size:12px;font-weight:500;line-height:32px;text-transform:uppercase;border:1px solid var(--white);color:var(--white)}
.tab.active{background:var(--blue);border-color:var(--blue)}
.pill{position:absolute;left:490px;top:208px;width:238px;height:48px;border-radius:24px;background:var(--orange);color:var(--white);font-weight:700;font-size:17px;line-height:48px;text-align:center;text-transform:uppercase;box-shadow:0 0 0 4px rgba(244,122,79,.35)}
.tree{position:absolute;left:0;top:0;width:1200px;height:772px}
.benefit{position:absolute;top:377px;width:240px;margin-left:-120px;text-align:center}
.benefit .badge{width:166px;height:166px;margin:0 auto}
.benefit h3{margin-top:46px;font-size:18px;font-weight:700;text-transform:uppercase}
.benefit p{margin-top:10px;font-family:"Open Sans",sans-serif;font-size:12.5px;line-height:19px;color:#e6e6e6}

/* who we are */
.who{height:505px}
.who .section-title{top:80px}
.who .lead{top:162px}
.value{position:absolute;top:250px;width:160px;margin-left:-80px;text-align:center}
.value .badge{width:124px;height:124px;margin:0 auto}
.value span{display:block;margin-top:22px;font-size:15px;font-weight:500;text-transform:uppercase}

/* press */
.press{height:490px;color:var(--white)}
.press-photo{position:absolute;inset:0;background:linear-gradient(180deg,#4aa7d8 0%,#3f9bd0 55%,#5aaedb 100%)}
.press .section-title{top:80px;color:var(--white)}
.press-sub{position:absolute;top:132px;left:0;right:0;text-align:center;font-family:"Open Sans",sans-serif;font-size:13px}
.card{position:absolute;top:193px;height:208px;background:var(--white);display:flex;box-shadow:0 3px 10px rgba(0,0,0,.15)}
.card-photo{height:100%;flex:none}
.card-body{padding:20px 22px;color:var(--ink)}
.card-body h4{font-size:15px;font-weight:500;line-height:22px;text-transform:uppercase}
.card-meta{margin-top:14px;display:flex;gap:22px;font-family:"Open Sans",sans-serif;font-size:12px;color:var(--muted);align-items:center}
.card-meta svg{width:13px;height:13px;margin-right:6px;vertical-align:-2px}
.card-body p{margin-top:14px;font-family:"Open Sans",sans-serif;font-size:12.5px;line-height:20px;color:var(--muted)}

/* contact */
.contact{height:534px;background:#f6f6f6}
.contact .section-title{top:60px}
.info{position:absolute;top:126px;display:flex;gap:14px;font-family:"Open Sans",sans-serif;font-size:13px;line-height:18px;color:var(--text)}
.info .ring{width:36px;height:36px;border-radius:50%;border:1px solid #f2c3b0;background:var(--white);display:flex;align-items:center;justify-content:center;flex:none}
.info svg{width:16px;height:16px}
.field{position:absolute;left:217px;width:335px;height:34px;background:var(--white);border:1px solid #e4e4e4;font-family:"Open Sans",sans-serif;font-size:11.5px;color:var(--text);padding:9px 12px}
.field.message{left:573px;top:202px;width:410px;height:188px}
.submit{position:absolute;left:481px;top:436px;width:238px;height:40px;background:var(--blue);color:var(--white);font-weight:700;font-size:14px;line-height:40px;text-align:center;text-transform:uppercase}

/* faq */
.faq{height:380px;background:var(--dark)}
.faq .section-title{top:72px;color:var(--white)}
.qa{position:absolute;left:172px;width:879px}
.q{height:34px;padding:0 16px;display:flex;align-items:center;justify-content:space-between;font-size:12px;font-weight:500;text-transform:uppercase;color:var(--white);background:var(--darker)}
.q.open{background:var(--orange)}
.q .toggle{width:14px;height:14px;border-radius:50%;background:var(--white);color:var(--dark);font-size:12px;line-height:14px;text-align:center;font-weight:700}
.q.open .toggle{color:var(--orange)}
.a{padding:14px 30px 16px;background:var(--darker);font-family:"Open Sans",sans-serif;font-size:13px;line-height:21px;color:#e8e8e8;border-top:1px solid #3a3a3a}

/* footer */
.site-footer{height:244px;background:var(--orange);color:var(--white)}
.site-footer .brand{left:100px;top:98px;font-size:44px;color:var(--white)}
.site-footer .brand-dot{background:var(--white)}
.copyright{position:absolute;left:470px;top:114px;font-family:"Open Sans",sans-serif;font-size:12px}
.social{position:absolute;right:105px;top:104px;display:flex;gap:14px}
.social span{width:38px;height:38px;border-radius:50%;border:2px solid var(--white)}
</style>
</head>
<body>

<header class="site-header">
  <div class="brand"><span class="brand-dot"></span>zapply</div>
  <div class="topbar">
    <svg viewBox="0 0 16 16"><path d="M4 1l3 3-2 2c1 2 3 4 5 5l2-2 3 3-2 2C7 14 2 9 2 3z" fill="var(--orange)"/></svg>
    <span>+971 5 23 47 90 12</span>
    <span class="sep">|</span>
    <svg viewBox="0 0 16 16"><rect x="1" y="3" width="14" height="10" rx="1" fill="var(--orange)"/><path d="M1 4l7 5 7-5" stroke="#fff" fill="none"/></svg>
    <span>info@zapplyhub.example</span>
  </div>
  <nav class="nav">
    <a class="active">HOME</a><a>HOW IT WORKS</a><a>BENEFIT</a><a>WHO WE ARE</a><a>PRESS</a><a>CONTACT</a><a>FAQ</a>
  </nav>
</header>

<section class="hero">
  <div class="hero-photo" role="img" aria-label="Photo of a couple relaxing in striped deck chairs on a tropical beach, toasting with drinks"></div>
  <div class="hero-word">zapply</div>
  <svg class="hero-wave" viewBox="0 0 1200 110" preserveAspectRatio="none">
    <path d="M0 70 C300 20 700 10 1200 40 L1200 110 L0 110 Z" fill="var(--orange)"/>
    <path d="M0 88 C300 38 700 28 1200 56 L1200 110 L0 110 Z" fill="var(--white)"/>
  </svg>
  <div class="hero-dots"><span class="on"></span><span></span><span></span></div>
</section>

<section class="how">
  <h2 class="section-title" style="top:38px">How it works</h2>
  <p class="lead" style="top:112px">zapply is a smart mobile app that the resort guests download it on their mobile. Through this app, the user locates himself and then can send orders. The resort receives the app requests on a dedicated POS, to ensure a seamless management of operation. The POS provides details of the requests as well as a summary of the daily activity and controls other aspect of the operation.</p>

  <div class="phone"><span class="cam"></span><div class="screen">zapply</div><span class="btn"></span></div>

  <svg class="flow" viewBox="0 0 1200 802">
    <defs>
      <marker id="arrowhead" viewBox="0 0 10 10" refX="8" refY="5" markerWidth="7" markerHeight="7" orient="auto"><path d="M0 0L10 5L0 10z" fill="#333"/></marker>
    </defs>
    <g stroke="#333" stroke-width="1.5" stroke-dasharray="4 4" fill="none" marker-end="url(#arrowhead)">
      <line x1="215" y1="378" x2="292" y2="490"/>
      <line x1="405" y1="560" x2="535" y2="605"/>
      <line x1="660" y1="605" x2="805" y2="560"/>
      <line x1="920" y1="492" x2="992" y2="388"/>
    </g>
  </svg>

  <div class="step" style="left:169px;top:285px">
    <svg class="badge" viewBox="0 0 112 112"><circle cx="56" cy="56" r="54" fill="none" stroke="var(--blue)" stroke-width="1.5"/><circle cx="56" cy="56" r="46" fill="var(--blue)"/><rect x="42" y="36" width="28" height="38" rx="2" fill="#fff"/><path d="M47 46h18M47 54h18M47 62h12" stroke="var(--blue)" stroke-width="2.5"/></svg>
    <div class="step-label">Check the menu</div>
  </div>
  <div class="step" style="left:342px;top:478px">
    <svg class="badge" viewBox="0 0 112 112"><circle cx="56" cy="56" r="54" fill="none" stroke="var(--orange)" stroke-width="1.5"/><circle cx="56" cy="56" r="46" fill="var(--orange)"/><path d="M36 66h40M40 62a16 16 0 0 1 32 0z" fill="#fff" stroke="#fff" stroke-width="3"/><circle cx="56" cy="43" r="3" fill="#fff"/></svg>
    <div class="step-label">Order the food<br>&amp; drinks</div>
  </div>
  <div class="step" style="left:597px;top:561px">
    <svg class="badge" viewBox="0 0 112 112"><circle cx="56" cy="56" r="54" fill="none" stroke="var(--blue)" stroke-width="1.5"/><circle cx="56" cy="56" r="46" fill="var(--blue)"/><circle cx="56" cy="44" r="10" fill="#fff"/><path d="M36 76a20 16 0 0 1 40 0z" fill="#fff"/></svg>
    <div class="step-label">Call the waiter</div>
  </div>
  <div class="step" style="left:873px;top:478px">
    <svg class="badge" viewBox="0 0 112 112"><circle cx="56" cy="56" r="54" fill="none" stroke="var(--orange)" stroke-width="1.5"/><circle cx="56" cy="56" r="46" fill="var(--orange)"/><circle cx="56" cy="46" r="8" fill="#fff"/><path d="M40 72a16 12 0 0 1 32 0z" fill="#fff"/><path d="M34 42h10M68 42h10" stroke="#fff" stroke-width="3"/></svg>
    <div class="step-label">Send requests to<br>the waiter</div>
  </div>
  <div class="step" style="left:1034px;top:285px">
    <svg class="badge" viewBox="0 0 112 112"><circle cx="56" cy="56" r="54" fill="none" stroke="var(--blue)" stroke-width="1.5"/><circle cx="56" cy="56" r="46" fill="var(--blue)"/><rect x="36" y="40" width="40" height="28" rx="3" fill="#fff"/><rect x="36" y="46" width="40" height="5" fill="var(--blue)"/></svg>
    <div class="step-label">Checkout &amp; pay</div>
  </div>
</section>

<section class="benefits">
  <div class="benefits-photo" role="img" aria-label="Dim photo of a cocktail glass on a bar at night"></div>
  <h2 class="section-title">Benefits</h2>
  <div class="tabs"><span class="tab active">For the guests</span><span class="tab">For the resort</span></div>
  <svg class="tree" viewBox="0 0 1200 772">
    <g stroke="#bdbdbd" stroke-width="1.5" fill="none">
      <path d="M609 256V335M208 377V335H1004V377M475 335V377M740 335V377"/>
    </g>
    <circle cx="470" cy="232" r="5" fill="var(--blue)"/>
    <circle cx="748" cy="232" r="5" fill="var(--blue)"/>
    <circle cx="575" cy="276" r="4" fill="var(--orange)"/>
    <circle cx="643" cy="276" r="4" fill="var(--orange)"/>
  </svg>
  <div class="pill">The guests</div>

  <div class="benefit" style="left:208px">
    <svg class="badge" viewBox="0 0 166 166"><circle cx="83" cy="83" r="80" fill="none" stroke="var(--blue)" stroke-width="5"/><circle cx="83" cy="83" r="68" fill="var(--blue)"/><rect x="60" y="52" width="46" height="62" rx="3" fill="#fff"/><path d="M70 70h26M70 80h26M70 90h18" stroke="var(--blue)" stroke-width="3"/></svg>
    <h3>Menu</h3>
    <p>see a visual for each item, and have all relevant dietary details</p>
  </div>
  <div class="benefit" style="left:475px">
    <svg class="badge" viewBox="0 0 166 166"><circle cx="83" cy="83" r="80" fill="none" stroke="var(--orange)" stroke-width="5"/><circle cx="83" cy="83" r="68" fill="var(--orange-dark)"/><circle cx="83" cy="87" r="30" fill="none" stroke="#fff" stroke-width="6"/><path d="M83 72v16l10 8" stroke="#fff" stroke-width="5" fill="none"/><path d="M58 58l10-8M108 58l-10-8" stroke="#fff" stroke-width="6"/></svg>
    <h3>Speed</h3>
    <p>No more time lost catching a waiter<br>Submit your orders</p>
  </div>
  <div class="benefit" style="left:740px">
    <svg class="badge" viewBox="0 0 166 166"><circle cx="83" cy="83" r="80" fill="none" stroke="var(--blue)" stroke-width="5"/><circle cx="83" cy="83" r="68" fill="var(--blue)"/><rect x="64" y="46" width="38" height="70" rx="5" fill="none" stroke="#fff" stroke-width="5"/><path d="M72 78l8 8 14-16" stroke="#fff" stroke-width="5" fill="none"/></svg>
    <h3>Customization</h3>
    <p>customize the order and avoid<br>human error</p>
  </div>
  <div class="benefit" style="left:1004px">
    <svg class="badge" viewBox="0 0 166 166"><circle cx="83" cy="83" r="80" fill="none" stroke="var(--orange)" stroke-width="5"/><circle cx="83" cy="83" r="68" fill="var(--orange)"/><rect x="54" y="60" width="58" height="40" rx="4" fill="#fff"/><rect x="54" y="68" width="58" height="8" fill="var(--orange)"/><rect x="62" y="86" width="18" height="5" fill="var(--orange)"/></svg>
    <h3>Fast checkout</h3>
    <p>Avoid waiting for the bill, use the saved credit card or cash</p>
  </div>
</section>

<section class="who">
  <h2 class="section-title">Who we are</h2>
  <p class="lead">zapply is a smart mobile app that the resort guests download it on their mobile. Through this app, the user locates himself and then can send orders. The resort receives the app requests on a dedicated POS, to ensure a seamless management of operation.</p>

  <div class="value" style="left:187px">
    <svg class="badge" viewBox="0 0 124 124"><circle cx="62" cy="62" r="60" fill="none" stroke="var(--orange)" stroke-width="2"/><circle cx="62" cy="62" r="52" fill="#fff" stroke="#f7c9b6" stroke-width="2"/><path d="M62 88c-12-16-18-24-18-34a18 18 0 0 1 36 0c0 10-6 18-18 34z" fill="var(--orange)"/><circle cx="62" cy="54" r="7" fill="#fff"/></svg>
    <span>Locate</span>
  </div>
  <div class="value" style="left:389px">
    <svg class="badge" viewBox="0 0 124 124"><circle cx="62" cy="62" r="60" fill="none" stroke="var(--blue)" stroke-width="2"/><circle cx="62" cy="62" r="52" fill="#fff" stroke="#b9dcf0" stroke-width="2"/><circle cx="57" cy="57" r="16" fill="none" stroke="var(--blue)" stroke-width="6"/><path d="M69 69l14 14" stroke="var(--blue)" stroke-width="8" stroke-linecap="round"/></svg>
    <span>Browse</span>
  </div>
  <div class="value" style="left:597px">
    <svg class="badge" viewBox="0 0 124 124"><circle cx="62" cy="62" r="60" fill="none" stroke="var(--orange)" stroke-width="2"/><circle cx="62" cy="62" r="52" fill="#fff" stroke="#f7c9b6" stroke-width="2"/><path d="M46 38h22l10 10v38H46z" fill="none" stroke="var(--orange)" stroke-width="4"/><path d="M53 58h18M53 66h18M53 74h12" stroke="var(--orange)" stroke-width="3"/></svg>
    <span>Order</span>
  </div>
  <div class="value" style="left:802px">
    <svg class="badge" viewBox="0 0 124 124"><circle cx="62" cy="62" r="60" fill="none" stroke="var(--blue)" stroke-width="2"/><circle cx="62" cy="62" r="52" fill="#fff" stroke="#b9dcf0" stroke-width="2"/><rect x="48" y="36" width="28" height="52" rx="4" fill="none" stroke="var(--blue)" stroke-width="4"/><circle cx="62" cy="80" r="2.5" fill="var(--blue)"/></svg>
    <span>Help</span>
  </div>
  <div class="value" style="left:1010px">
    <svg class="badge" viewBox="0 0 124 124"><circle cx="62" cy="62" r="60" fill="none" stroke="var(--orange)" stroke-width="2"/><circle cx="62" cy="62" r="52" fill="#fff" stroke="#f7c9b6" stroke-width="2"/><rect x="38" y="46" width="48" height="32" rx="2" fill="var(--orange)"/><rect x="44" y="52" width="36" height="20" fill="none" stroke="#fff" stroke-width="2"/><circle cx="62" cy="62" r="6" fill="#fff"/></svg>
    <span>Pay</span>
  </div>
</section>

<section class="press">
  <div class="press-photo" role="img" aria-label="Soft blurred photo of a pool with a flower in the foreground"></div>
  <h2 class="section-title">In the press</h2>
  <p class="press-sub">Read The Latest Articles Regarding The Products And Accessories</p>

  <article class="card" style="left:98px;width:487px">
    <div class="card-photo" style="width:220px;background:linear-gradient(135deg,#8fae5a,#d98a3b 55%,#f3e6cf)" role="img" aria-label="Photo of a plated meal and a cold drink on a resort table"></div>
    <div class="card-body">
      <h4>Lorem ipsum is simply the dummy text printing</h4>
      <div class="card-meta"><span><svg viewBox="0 0 14 14"><rect x="1" y="2" width="12" height="11" fill="none" stroke="var(--orange)"/><path d="M1 5h12" stroke="var(--orange)"/></svg>August 01</span><span><svg viewBox="0 0 14 14"><circle cx="7" cy="5" r="3" fill="var(--orange)"/><path d="M2 13a5 4 0 0 1 10 0z" fill="var(--orange)"/></svg>Rami</span></div>
      <p>It is a long established fact that a reader will be distracted by the readable content of a page when looking at its layout.</p>
    </div>
  </article>
  <article class="card" style="left:618px;width:481px">
    <div class="card-photo" style="width:182px;background:linear-gradient(135deg,#e9d2b0,#c98f63 55%,#7a4a34)" role="img" aria-label="Photo of a smiling guest in a sun hat at a restaurant table"></div>
    <div class="card-body">
      <h4>Lorem ipsum is simply the dummy text printing</h4>
      <div class="card-meta"><span><svg viewBox="0 0 14 14"><rect x="1" y="2" width="12" height="11" fill="none" stroke="var(--orange)"/><path d="M1 5h12" stroke="var(--orange)"/></svg>August 01</span><span><svg viewBox="0 0 14 14"><circle cx="7" cy="5" r="3" fill="var(--orange)"/><path d="M2 13a5 4 0 0 1 10 0z" fill="var(--orange)"/></svg>Rami</span></div>
      <p>It is a long established fact that a reader will be distracted by the readable content of a page when looking at its layout.</p>
    </div>
  </article>
</section>

<section class="contact">
  <h2 class="section-title">Contact us</h2>
  <div class="info" style="left:217px">
    <span class="ring"><svg viewBox="0 0 16 16"><path d="M8 15C4 10 3 8 3 6a5 5 0 0 1 10 0c0 2-1 4-5 9z" fill="var(--orange)"/><circle cx="8" cy="6" r="2" fill="#fff"/></svg></span>
    <span>zapply, Harbor Quarter, Dubai,<br>United Arab Emirates</span>
  </div>
  <div class="info" style="left:535px">
    <span class="ring"><svg viewBox="0 0 16 16"><path d="M4 1l3 3-2 2c1 2 3 4 5 5l2-2 3 3-2 2C7 14 2 9 2 3z" fill="var(--orange)"/></svg></span>
    <span>Call Us :<br>+971 5 23 47 90 12</span>
  </div>
  <div class="info" style="left:810px">
    <span class="ring"><svg viewBox="0 0 16 16"><rect x="1" y="3" width="14" height="10" rx="1" fill="none" stroke="var(--orange)" stroke-width="1.5"/><path d="M1 4l7 5 7-5" stroke="var(--orange)" fill="none" stroke-width="1.5"/></svg></span>
    <span>E - Mail :<br>info@zapplyhub.example</span>
  </div>

  <div class="field" style="top:202px">First Name*</div>
  <div class="field" style="top:254px">Last Name*</div>
  <div class="field" style="top:306px">E-Mail Address*</div>
  <div class="field" style="top:358px">Phone Number*</div>
  <div class="field message">Message*</div>
  <div class="submit">Submit now</div>
</section>

<section class="faq">
  <h2 class="section-title">FAQ</h2>
  <div class="qa" style="top:136px">
    <div class="q open"><span>Q1: Lorem ipsum is simply dummy text of the printing and typesetting industry</span><span class="toggle">−</span></div>
    <div class="a">Lorem Ipsum has been the industry's standard dummy text ever since the 1500s, when an unknown printer took a galley of type and scrambled it to make a type specimen book. It has survived not only five centuries</div>
  </div>
  <div class="qa" style="top:262px"><div class="q"><span>Q2: Lorem ipsum is simply dummy text of the printing and typesetting industry</span><span class="toggle">+</span></div></div>
  <div class="qa" style="top:302px"><div class="q"><span>Q3: Lorem ipsum is simply dummy text of the printing and typesetting industry</span><span class="toggle">+</span></div></div>
  <div class="qa" style="top:342px"><div class="q"><span>Q4: Lorem ipsum is simply dummy text of the printing and typesetting industry</span><span class="toggle">+</span></div></div>
</section>

<footer class="site-footer">
  <div class="brand"><span class="brand-dot"></span>zapply</div>
  <p class="copyright">© Copyright 2017 Zapply. All Rights Reserved</p>
  <div class="social"><span></span><span></span><span></span><span></span></div>
</footer>

</body>
</html>
```